Design for Pediatric Occupational Therapist who works with children with special needs

I need 2 x 2 sq business cards and post cards for my Pediatric Occupational Therapy business. We work with children with special needs and help them learn skills for daily living (eating, writing, dressing, etc). We're looking for a colorful design (not loud) that looks professional and helps it stand out from other cards. I want to avoid many of the standard designs that you see on Pella press which are used my many other Pediatric OT's. The design will be intended for business cards, post cards and hopefully can also be used on company letterhead. I'll upload a current copy of the logo we currently use on company letter head so you get an idea of the design we've been using to date. This image does not need to be used again, but serves more as a reference to the design used in the past. The winning designer will likely be hired to design a custom logo for letter head.

Target Market(s)

Families of children with special needs, pediatricians

Industry/Entity Type

Business

Contact Information for Business Card

I need a logo or design for 2 x 2 sq business cards and post cards for my Pediatric Occupational Therapy business. We work with children with special needs and help them learn skills for daily living (eating, writing, dressing, etc). We're looking for a colorful design (not loud) that looks professional and helps it stand out from other cards. I want to avoid many of the standard designs that you see on Pella press which are used my many other Pediatric OT's. The design will be intended for business cards, post cards and hopefully can also be used on company letterhead. I'll upload a current copy of the logo we currently use on company letter head so you get an idea of the design we've been using to date.

Font styles to use
Sans Serif

Requirements
Must have
• Area to include company name, address, phone, etc.
• Company name = Brightway Care Partners

```html
<!DOCTYPE html>
<html lang="en">
<head>
<meta charset="utf-8">
<title>Brightway Care Partners – Square Business Card</title>
<link rel="stylesheet" href="https://fonts.googleapis.com/css2?family=Amatic+SC:wght@700&family=Montserrat:wght@500;600;700&display=swap">
<style>
  :root {
    --backdrop: #f2c600;
    --red: #e93d5f;
    --orange: #f2824a;
    --yellow: #ffc90a;
    --teal: #5fbfa8;
    --sky: #59b3e6;
    --indigo: #6462ab;
    --violet: #8f5ba6;
    --ink: #111111;
    --paper: #ffffff;
  }
  * { box-sizing: border-box; margin: 0; padding: 0; }
  html, body { width: 1200px; height: 1200px; overflow: hidden; }
  body { background: var(--backdrop); position: relative; font-family: "Montserrat", sans-serif; }

  .card { position: absolute; width: 468px; height: 468px; overflow: hidden; }
  .card--front { left: 67px; top: 363px; background: var(--paper); }
  .card--back { left: 639px; top: 363px; }

  .stripe-band { position: absolute; left: 0; width: 100%; height: 62px; display: flex; }
  .stripe-band--top { top: 0; }
  .stripe-band--bottom { bottom: 0; }
  .stripe-band span { display: block; height: 100%; }

  .s-red { background: var(--red); }
  .s-orange { background: var(--orange); }
  .s-yellow { background: var(--yellow); }
  .s-teal { background: var(--teal); }
  .s-sky { background: var(--sky); }
  .s-indigo { background: var(--indigo); }
  .s-violet { background: var(--violet); }

  .contact-block { position: absolute; top: 62px; bottom: 62px; left: 0; right: 0; display: flex; flex-direction: column; align-items: center; justify-content: center; }
  .person-name { font-family: "Amatic SC", cursive; font-weight: 700; font-size: 50px; letter-spacing: 1px; color: var(--ink); line-height: 1; }
  .credential { font-weight: 600; font-size: 19px; letter-spacing: 1px; color: var(--ink); margin-top: 0; }
  .name-rule { width: 172px; height: 5px; background: var(--ink); margin-top: 6px; margin-bottom: 44px; }
  .contact-line { display: flex; align-items: center; gap: 4px; font-weight: 500; font-size: 21px; letter-spacing: 1.4px; color: var(--ink); line-height: 1.15; }
  .contact-icon { width: 17px; height: 17px; flex: none; }

  .stripe-field { position: absolute; inset: 0; display: flex; }
  .stripe-field span { flex: 1; height: 100%; }

  .brand-block { position: absolute; left: 0; right: 0; top: 190px; text-align: center; color: var(--paper); }
  .brand-name { font-weight: 700; font-size: 32px; line-height: 1.1; letter-spacing: 0.5px; }
  .brand-tagline { font-weight: 700; font-size: 17px; letter-spacing: 0.2px; margin-top: 22px; }
</style>
</head>
<body>

  <section class="card card--front" aria-label="Business card front">
    <div class="stripe-band stripe-band--top">
      <span class="s-red" style="width:47px"></span><span class="s-orange" style="width:75px"></span><span class="s-yellow" style="width:76px"></span><span class="s-teal" style="width:76px"></span><span class="s-sky" style="width:76px"></span><span class="s-indigo" style="width:74px"></span><span class="s-violet" style="width:44px"></span>
    </div>

    <div class="contact-block">
      <h1 class="person-name">MARISOL VEGA</h1>
      <p class="credential">OTR/L</p>
      <div class="name-rule"></div>
      <p class="contact-line">
        <svg class="contact-icon" viewBox="0 0 20 20" aria-hidden="true"><circle cx="10" cy="10" r="10" fill="#e93d5f"/><path d="M6.6 5.2c.4-.3 1-.3 1.3.1l1.1 1.6c.3.4.2.9-.1 1.2l-.7.6c.5 1.1 1.4 2 2.5 2.6l.6-.7c.3-.4.9-.4 1.2-.1l1.6 1.1c.4.3.5.9.1 1.3l-.8.9c-.5.5-1.3.7-2 .4-2.4-1-4.3-2.9-5.3-5.3-.3-.7-.1-1.5.4-2z" fill="#fff"/></svg>
        412.555.0176
      </p>
      <p class="contact-line">
        <svg class="contact-icon" viewBox="0 0 20 20" aria-hidden="true"><circle cx="10" cy="10" r="10" fill="#8f5ba6"/><rect x="5" y="6.5" width="10" height="7" rx="1" fill="#fff"/><path d="M5.5 7l4.5 3.4L14.5 7" stroke="#8f5ba6" stroke-width="1.1" fill="none"/></svg>
        marisol.v@brightway.net
      </p>
    </div>

    <div class="stripe-band stripe-band--bottom">
      <span class="s-red" style="width:47px"></span><span class="s-orange" style="width:75px"></span><span class="s-yellow" style="width:76px"></span><span class="s-teal" style="width:76px"></span><span class="s-sky" style="width:76px"></span><span class="s-indigo" style="width:74px"></span><span class="s-violet" style="width:44px"></span>
    </div>
  </section>

  <section class="card card--back" aria-label="Business card back">
    <div class="stripe-field" role="img" aria-label="Rainbow stripes with a scattered pattern of children's handprints">
      <span class="s-red"></span><span class="s-orange"></span><span class="s-yellow"></span><span class="s-teal"></span><span class="s-sky"></span><span class="s-indigo"></span><span class="s-violet"></span>
    </div>
    <div class="brand-block">
      <h2 class="brand-name">Brightway Care Partners</h2>
      <p class="brand-tagline">PEDIATRIC OCCUPATIONAL THERAPY</p>
    </div>
  </section>

</body>
</html>
```